Business Card Design

Selling Televisions, Velmora, Kira, Dravelux, Ronavi
The latest models, sizes ranging from 22"- 75"
Surround Sounds, Sound Bars and Wall Mounts

Target Market(s)

Mainly males/boys/blokes etc

Industry/Entity Type

Business

Contact Information for Business Card

Glen Marsh
07841526094
glmarsh@quinvale-mail.com

Requirements
Must have
• simplistic design, probably just 2 of the images used

clarity essential
Nice to have
• Metallic if possible

```html
<!DOCTYPE html>
<html lang="en">
<head>
<meta charset="utf-8">
<title>Glen Marsh – Business Card</title>
<link rel="stylesheet" href="https://fonts.googleapis.com/css2?family=Open+Sans:wght@600;700&display=swap">
<style>
  :root {
    --stage: #1d1d1d;
    --name-violet: #5a4fa6;
    --detail-ink: #1a1a1a;
    --scene-sky: #d9dcd8;
    --scene-window: #c9c3b4;
    --scene-room: #e6e6e4;
    --scene-floor: #b9a48c;
    --scene-accent: #6a4f8c;
  }
  html, body {
    margin: 0;
    padding: 0;
    width: 1200px;
    height: 944px;
    overflow: hidden;
    background: var(--stage);
    font-family: "Open Sans", Arial, sans-serif;
  }
  .business-card {
    position: absolute;
    left: 100px;
    top: 186px;
    width: 1000px;
    height: 572px;
    overflow: hidden;
    background: var(--scene-room);
  }
  .room-scene {
    position: absolute;
    inset: 0;
    background:
      linear-gradient(160deg,
        var(--scene-sky) 0%,
        var(--scene-window) 30%,
        var(--scene-room) 55%,
        var(--scene-accent) 62%,
        var(--scene-room) 70%,
        var(--scene-floor) 100%);
    opacity: 0.85;
  }
  .contact-block {
    position: absolute;
    left: 92px;
    top: 318px;
  }
  .contact-name {
    margin: 0 0 14px;
    font-size: 46px;
    font-weight: 700;
    color: var(--name-violet);
    letter-spacing: 0.2px;
  }
  .contact-line {
    margin: 0 0 6px;
    font-size: 22px;
    font-weight: 700;
    color: var(--detail-ink);
  }
</style>
</head>
<body>
  <section class="business-card">
    <div class="room-scene" role="img" aria-label="Photograph of a bright living room with a large curved television showing a sunset, a riverside city view through the windows, a navy cushion and white roses"></div>
    <div class="contact-block">
      <h1 class="contact-name">Glen Marsh</h1>
      <p class="contact-line">P: 07841526094</p>
      <p class="contact-line">E: glmarsh@quinvale-mail.com</p>
    </div>
  </section>
</body>
</html>
```